Create a basic website for a new air cargo consultancy, called 'Veltrane Loadwise'

We want to build a basic website (homepage, 'about us' page, services and contact us page).
We have a logo, we have most of the text to be inserted, but not all. We also still need to take pictures.
We would like to have a fresh and modern, but business like design and the creation of the website.
We want to be able to modify the website after (add pictures and more text, update references).
We already have a url.

```html
<!DOCTYPE html>
<html lang="en">
<head>
<meta charset="utf-8">
<title>Veltrane Loadwise</title>
<link href="https://fonts.googleapis.com/css2?family=Josefin+Sans:wght@400;600;700&family=Poppins:wght@400;500;600&display=swap" rel="stylesheet">
<style>
:root{
  --blue:#2b3590;
  --blue-soft:#3e49a8;
  --gold:#d39e2a;
  --ink:#222;
  --muted:#666;
  --line:#c9c9c9;
  --paper:#ffffff;
  --mist:#f7f7f7;
  --night:#161616;
}
*{box-sizing:border-box;margin:0;padding:0}
html,body{width:1200px;height:3240px;overflow:hidden}
body{position:relative;background:var(--paper);font-family:"Poppins",sans-serif;color:var(--ink)}
.abs{position:absolute}
.head-font{font-family:"Josefin Sans",sans-serif}
.btn{position:absolute;display:flex;align-items:center;justify-content:center;background:var(--gold);color:#fff;font-family:"Josefin Sans",sans-serif;font-size:15px;font-weight:600;letter-spacing:.3px}
.ph{position:absolute}

/* hero */
.hero{position:absolute;left:0;top:0;width:1200px;height:700px;background:var(--blue)}
.hero-photo{position:absolute;left:0;top:0;width:1200px;height:700px;background:linear-gradient(135deg,#c9cfd6,#8e96a3 55%,#4a4f60);clip-path:polygon(650px 0,1200px 0,1200px 700px,558px 700px)}
.nav-bar{position:absolute;left:75px;top:0;width:1050px;height:88px;background:#fff;display:flex;align-items:center}
.brand{position:absolute;left:18px;top:26px;display:flex;align-items:center;gap:8px;font-family:"Josefin Sans",sans-serif;font-weight:700;font-size:21px;color:var(--blue)}
.brand i{width:14px;height:14px;background:var(--gold);display:block}
.nav{position:absolute;left:297px;top:36px;display:flex;gap:0;font-family:"Josefin Sans",sans-serif;font-size:15px;color:#444}
.nav span{position:absolute;white-space:nowrap}
.hero h1{position:absolute;left:83px;top:250px;font-family:"Josefin Sans",sans-serif;font-weight:700;font-size:41px;color:#fff;letter-spacing:.5px}
.hero p{position:absolute;left:83px;top:310px;width:460px;font-size:16.5px;line-height:22px;color:#fff;font-family:"Josefin Sans",sans-serif}
.btn-ghost{position:absolute;display:flex;align-items:center;justify-content:center;border:2px solid #fff;color:#fff;font-family:"Josefin Sans",sans-serif;font-size:15px;font-weight:600}
.stats{position:absolute;left:78px;top:611px;width:1050px;height:142px;background:#fff;box-shadow:0 18px 40px rgba(0,0,0,.08)}
.stat{position:absolute;top:18px;display:flex;align-items:center;gap:16px}
.stat b{display:block;font-family:"Josefin Sans",sans-serif;font-size:42px;color:var(--blue);line-height:44px}
.stat em{display:block;font-style:normal;font-family:"Josefin Sans",sans-serif;font-weight:600;font-size:16px;color:#444;line-height:23px;text-transform:uppercase}

/* about */
.about-photo{left:36px;top:894px;width:500px;height:380px;background:linear-gradient(120deg,#d8dde3,#9aa2ad 60%,#5c6271);clip-path:polygon(0 0,500px 0,460px 380px,0 380px)}
.stripes{background:var(--gold);opacity:.9}
.section-title{font-family:"Josefin Sans",sans-serif;font-weight:700;font-size:28px;color:var(--blue)}
.about-text{left:623px;top:1030px;width:480px;font-size:15.5px;line-height:27.7px;color:var(--muted)}

/* services */
.services{left:0;top:1383px;width:1200px;height:552px;background:linear-gradient(180deg,#4a54b0,var(--blue) 70%)}
.card{position:absolute;top:1592px;width:222px;height:443px;background:#fff;border:1px solid #cfd0de;border-radius:111px;text-align:center}
.card .pic{position:absolute;left:17px;top:18px;width:188px;height:188px;border-radius:50%;border:5px solid var(--blue)}
.card h3{position:absolute;left:10px;right:10px;top:235px;font-family:"Poppins",sans-serif;font-weight:600;font-size:21px;line-height:25px;color:#111}
.card p{position:absolute;left:22px;right:22px;top:297px;font-size:10px;line-height:17px;color:#888}
.go{position:absolute;top:2007px;width:52px;height:52px;border-radius:50%;background:var(--gold);display:flex;align-items:center;justify-content:center}

/* contact */
.contact{left:0;top:2202px;width:1200px;height:498px;background:var(--mist)}
.contact-photo{left:0;top:2202px;width:1200px;height:498px;background:linear-gradient(140deg,#e3e6ea,#a7adb6 50%,#2f3445);clip-path:polygon(742px 0,1200px 0,1200px 498px,625px 498px)}
.field{position:absolute;background:#fff;border:1.5px solid var(--line);font-size:9px;color:#999;padding:12px 16px}

/* footer */
.footer{left:0;top:2700px;width:1200px;height:540px;background:var(--night);color:#8c8c8c}
.foot-brand{left:74px;top:2845px;width:277px;height:137px;background:#fff;border-bottom:4px solid var(--blue);display:flex;align-items:center;justify-content:center;gap:10px;font-family:"Josefin Sans",sans-serif;font-weight:700;font-size:23px;color:var(--blue)}
.foot-brand i{width:16px;height:16px;background:var(--gold);display:block}
.foot-h{font-family:"Poppins",sans-serif;font-weight:500;font-size:23px;color:#fff}
.qlink{position:absolute;left:447px;display:flex;align-items:center;gap:10px;font-size:14px;color:#7b7b7b}
.cline{position:absolute;left:657px;display:flex;align-items:center;gap:12px;font-size:17px;color:#9a9a9a}
</style>
</head>
<body>

<header class="hero">
  <div class="hero-photo" role="img" aria-label="Photo of two business consultants reviewing an orange folder in an airport terminal"></div>
  <div class="nav-bar">
    <div class="brand"><i></i>Veltrane Loadwise</div>
    <nav class="nav">
      <span style="left:0">HOME</span>
      <span style="left:92px">ABOUT</span>
      <span style="left:197px">SERVICES</span>
      <span style="left:317px;top:2px">BLOG</span>
      <span style="left:417px">CONTACT</span>
    </nav>
    <div class="btn" style="left:862px;top:23px;width:148px;height:40px;font-size:15px">GET STARTED</div>
  </div>
  <h1>VELTRANE LOADWISE</h1>
  <p>Welcome to Veltrane Loadwise, your premier consultancy specialized in the air cargo sector.</p>
  <div class="btn" style="left:84px;top:430px;width:148px;height:40px">OUR SERVICES</div>
  <div class="btn-ghost" style="left:242px;top:430px;width:149px;height:41px">GET STARTED</div>
</header>

<section class="stats">
  <div class="stat" style="left:90px">
    <svg width="86" height="86" viewBox="0 0 86 86"><circle cx="48" cy="40" r="30" fill="var(--gold)"/><path d="M16 76 L70 50 M22 30 l6 6 M10 50 h8" stroke="var(--blue)" stroke-width="4" fill="none" stroke-linecap="round"/><rect x="30" y="28" width="30" height="26" rx="5" fill="none" stroke="var(--blue)" stroke-width="4"/></svg>
    <div><b>99%</b><em>Consulting<br>Success</em></div>
  </div>
  <div class="stat" style="left:405px">
    <svg width="76" height="86" viewBox="0 0 76 86"><circle cx="38" cy="42" r="34" fill="var(--gold)"/><circle cx="26" cy="26" r="7" fill="none" stroke="var(--blue)" stroke-width="3.5"/><circle cx="50" cy="26" r="7" fill="none" stroke="var(--blue)" stroke-width="3.5"/><path d="M6 58 L26 44 L38 56 L50 44 L70 58 L50 76 L26 76Z" fill="none" stroke="var(--blue)" stroke-width="3.5" stroke-linejoin="round"/></svg>
    <div><b>22K+</b><em>Worldwide<br>Client</em></div>
  </div>
  <div class="stat" style="left:712px;top:26px">
    <svg width="78" height="80" viewBox="0 0 78 80"><circle cx="39" cy="36" r="30" fill="var(--gold)"/><circle cx="39" cy="36" r="16" fill="none" stroke="var(--blue)" stroke-width="3.5"/><path d="M31 36 l6 6 l10 -12" stroke="var(--blue)" stroke-width="3.5" fill="none"/><path d="M24 60 l-8 18 l10 -4 M54 60 l8 18 l-10 -4" stroke="var(--blue)" stroke-width="3.5" fill="none"/></svg>
    <div><b>12+</b><em>Years of<br>Eperience</em></div>
  </div>
</section>

<section>
  <div class="ph about-photo" role="img" aria-label="Photo of two travellers walking through an airport with a phone and a notebook"></div>
  <div class="ph stripes" role="img" aria-label="Gold diagonal stripe accent" style="left:272px;top:1162px;width:311px;height:91px;clip-path:polygon(14px 0,311px 0,297px 91px,0 91px)"></div>
  <h2 class="abs section-title" style="left:623px;top:957px">ABOUT US</h2>
  <p class="abs about-text">Welcome to Veltrane Loadwise, your premier consultancy specialized in the air cargo sector. We are dedicated to helping clients enhance their overall cargo strategy, drive digital transformation, fostercommunity building, and achieve sustainability goals.</p>
  <div class="btn" style="left:616px;top:1208px;width:147px;height:39px">READ MORE</div>
</section>

<section>
  <div class="abs services" role="img" aria-label="Faded photo of aircraft tails on an airport apron tinted blue"></div>
  <h2 class="abs head-font" style="left:0;width:1220px;text-align:center;top:1485px;font-size:28px;font-weight:600;color:#fff">OUR SERVICES</h2>

  <div class="card" style="left:94px">
    <div class="pic" role="img" aria-label="Photo of a team meeting around a laptop" style="background:linear-gradient(135deg,#c9b8a4,#7d6a5e)"></div>
    <h3>Strategic<br>Planning</h3>
    <p>We help you navigate the complexities of the global cargo landscape, ensuring your business stays competitive and resilient.</p>
  </div>
  <div class="card" style="left:364px">
    <div class="pic" role="img" aria-label="Photo of a consultant working on a laptop" style="background:linear-gradient(135deg,#e3d9d4,#b3403f)"></div>
    <h3 style="top:245px">Digitalization</h3>
    <p>We help you navigate the complexities of the global cargo landscape, ensuring your business stays competitive and resilient.</p>
  </div>
  <div class="card" style="left:633px">
    <div class="pic" role="img" aria-label="Photo of a group gathered around a laptop outdoors" style="background:linear-gradient(135deg,#9c8d82,#4d4845)"></div>
    <h3>Community<br>Building</h3>
    <p>We help you navigate the complexities of the global cargo landscape, ensuring your business stays competitive and resilient.</p>
  </div>
  <div class="card" style="left:902px">
    <div class="pic" role="img" aria-label="Photo of two colleagues reviewing documents at a desk" style="background:linear-gradient(135deg,#d9d6d0,#8c6f62)"></div>
    <h3 style="top:245px">Sustainability</h3>
    <p>We help you navigate the complexities of the global cargo landscape, ensuring your business stays competitive and resilient.</p>
  </div>

  <div class="go" style="left:180px"><svg width="22" height="22" viewBox="0 0 22 22"><path d="M2 8h9V3l9 8-9 8v-5H2z" fill="#fff"/></svg></div>
  <div class="go" style="left:449px"><svg width="22" height="22" viewBox="0 0 22 22"><path d="M2 8h9V3l9 8-9 8v-5H2z" fill="#fff"/></svg></div>
  <div class="go" style="left:718px"><svg width="22" height="22" viewBox="0 0 22 22"><path d="M2 8h9V3l9 8-9 8v-5H2z" fill="#fff"/></svg></div>
  <div class="go" style="left:987px"><svg width="22" height="22" viewBox="0 0 22 22"><path d="M2 8h9V3l9 8-9 8v-5H2z" fill="#fff"/></svg></div>
</section>

<section>
  <div class="abs contact"></div>
  <div class="ph contact-photo" role="img" aria-label="Photo of three business people listening at a conference table"></div>
  <div class="ph stripes" role="img" aria-label="Gold diagonal stripe accent" style="left:616px;top:2575px;width:309px;height:89px;clip-path:polygon(14px 0,309px 0,295px 89px,0 89px)"></div>
  <h2 class="abs section-title" style="left:78px;top:2288px">CONTACT US</h2>
  <div class="field" style="left:80px;top:2348px;width:246px;height:31px;padding-top:11px">Name</div>
  <div class="field" style="left:344px;top:2348px;width:246px;height:31px;padding-top:11px">Phone</div>
  <div class="field" style="left:80px;top:2392px;width:246px;height:31px;padding-top:11px">Email</div>
  <div class="field" style="left:344px;top:2392px;width:246px;height:31px;padding-top:11px">Subject</div>
  <div class="field" style="left:80px;top:2443px;width:510px;height:110px;padding:14px 26px">Message</div>
  <div class="btn" style="left:80px;top:2578px;width:120px;height:32px;font-size:12px">SEND NOW</div>
</section>

<footer>
  <div class="abs footer"></div>
  <div class="abs foot-brand"><i></i>Veltrane Loadwise</div>
  <p class="abs" style="left:74px;top:2992px;width:320px;font-size:13px;line-height:16px;color:#8c8c8c">Welcome to Veltrane Loadwise, your premier consultancy specialized in the air cargo sector.</p>

  <h4 class="abs foot-h" style="left:449px;top:2847px">Quick Links</h4>
  <div class="qlink" style="top:2906px"><svg width="26" height="26" viewBox="0 0 26 26"><circle cx="13" cy="13" r="11.5" fill="none" stroke="var(--gold)" stroke-width="1.6"/><path d="M7 13h11M14 9l4 4-4 4" stroke="var(--gold)" stroke-width="1.6" fill="none"/></svg>HOME</div>
  <div class="qlink" style="top:2956px"><svg width="26" height="26" viewBox="0 0 26 26"><circle cx="13" cy="13" r="11.5" fill="none" stroke="var(--gold)" stroke-width="1.6"/><path d="M7 13h11M14 9l4 4-4 4" stroke="var(--gold)" stroke-width="1.6" fill="none"/></svg>ABOUT</div>
  <div class="qlink" style="top:3000px"><svg width="26" height="26" viewBox="0 0 26 26"><circle cx="13" cy="13" r="11.5" fill="none" stroke="var(--gold)" stroke-width="1.6"/><path d="M7 13h11M14 9l4 4-4 4" stroke="var(--gold)" stroke-width="1.6" fill="none"/></svg>SERVICES</div>
  <div class="qlink" style="top:3046px"><svg width="26" height="26" viewBox="0 0 26 26"><circle cx="13" cy="13" r="11.5" fill="none" stroke="var(--gold)" stroke-width="1.6"/><path d="M7 13h11M14 9l4 4-4 4" stroke="var(--gold)" stroke-width="1.6" fill="none"/></svg>BLOG</div>
  <div class="qlink" style="top:3094px"><svg width="26" height="26" viewBox="0 0 26 26"><circle cx="13" cy="13" r="11.5" fill="none" stroke="var(--gold)" stroke-width="1.6"/><path d="M7 13h11M14 9l4 4-4 4" stroke="var(--gold)" stroke-width="1.6" fill="none"/></svg>CONTACT</div>

  <h4 class="abs foot-h" style="left:665px;top:2848px">Contact</h4>
  <div class="cline" style="top:2904px"><svg width="40" height="40" viewBox="0 0 40 40"><circle cx="20" cy="20" r="18.5" fill="none" stroke="var(--gold)" stroke-width="2"/><path d="M13 11c-2 2-2 6 2 11s9 8 12 7l2-3-4-3-2 2c-2-1-5-4-6-6l2-2-3-4z" fill="var(--gold)"/></svg>(+00)555 014 220</div>
  <div class="cline" style="top:2973px"><svg width="40" height="40" viewBox="0 0 40 40"><circle cx="20" cy="20" r="18.5" fill="none" stroke="var(--gold)" stroke-width="2"/><rect x="11" y="16" width="18" height="12" fill="var(--gold)"/><path d="M11 16l9-5 9 5-9 6z" fill="var(--gold)" stroke="var(--night)" stroke-width="1"/></svg>hello@veltrane-mail.test</div>
  <div class="cline" style="top:3047px"><svg width="40" height="40" viewBox="0 0 40 40"><circle cx="20" cy="20" r="18.5" fill="none" stroke="var(--gold)" stroke-width="2"/><path d="M20 30s-7-8-7-13a7 7 0 0 1 14 0c0 5-7 13-7 13z" fill="none" stroke="var(--gold)" stroke-width="2.2"/><circle cx="20" cy="17" r="2.5" fill="var(--gold)"/></svg>&nbsp;Jl. Harbor Line No.12, Sentra</div>

  <h4 class="abs foot-h" style="left:952px;top:2848px">Subscribe</h4>
  <div class="abs" style="left:952px;top:2920px;width:185px;height:47px;border-radius:24px;background:#fff;font-size:16px;color:#555;padding:14px 22px">Email Address</div>
  <div class="abs" style="left:952px;top:2988px;width:185px;height:46px;border-radius:23px;background:var(--gold);color:#fff;font-family:'Josefin Sans',sans-serif;font-weight:700;font-size:16px;display:flex;align-items:center;justify-content:center">SUBSCRIBE NOW</div>

  <p class="abs" style="left:74px;top:3204px;font-size:14px;color:#7b7b7b">© Copyright 2024, All Rights Reserved.</p>
  <p class="abs" style="right:56px;top:3204px;font-size:14px;color:#7b7b7b">Privacy Policy | Term &amp; Conditions</p>
</footer>

</body>
</html>
```